Business Card / Appointment Card for Physician

On one side it should give the logo, address, and contact information, and on the other side it should br an Appointment card.

One Side:
Logo (see attached files)
Board Certified American Orthopedic Surgery

1874 Larkmoor Ave.
Suite KP7
Bronx, NY 10287
Tel: (718) 555 - 0142
Fax: (718) 555 - 0187

612 Ninth Ave.
Suite 42
New York, NY 10089
Tel: (212) 555 - 0163

Second Side:
Appointment
give them a choice of Bronx or Mahattan office
For:
Date:
Time:

If you are unable to keep your appointment, please call (718) 555-0129 24hrs in advance.

Target Market(s)

People that need orthopedic surgery

Industry/Entity Type

Business

Contact Information for Business Card

smart and attractive

Requirements
Must have
• logo
• contact information on one side, appointment information on the other

```html
<!DOCTYPE html>
<html lang="en">
<head>
<meta charset="utf-8">
<title>Daniel R. Hollister MD PC — Stationery</title>
<link href="https://fonts.googleapis.com/css2?family=Montserrat:wght@400;500;600;700&family=Noto+Serif:wght@400;700&display=swap" rel="stylesheet">
<style>
  :root{
    --bg:#d9dbde;
    --paper:#ffffff;
    --card:#eeeeef;
    --blue:#0a68a8;
    --sky:#2a95d5;
    --green:#8cc153;
    --ink:#3a3f45;
    --rule:#9aa3ab;
  }
  *{box-sizing:border-box;margin:0;padding:0}
  html,body{width:1200px;height:972px;overflow:hidden}
  body{background:var(--bg);font-family:"Montserrat",sans-serif;color:var(--ink);position:relative}
  .icons{position:absolute;width:0;height:0}

  /* shared logo */
  .brand{display:flex;align-items:center;gap:8px}
  .brand-dot{width:28px;height:28px;border-radius:50%;background:var(--sky);flex:none}
  .brand-text{display:flex;flex-direction:column}
  .brand-name{font-weight:700;color:var(--blue);font-size:15px;letter-spacing:.2px;line-height:1.1;white-space:nowrap}
  .brand-tag{font-weight:700;color:var(--blue);font-size:7px;letter-spacing:.2px;margin-top:3px;white-space:nowrap}

  .contact{font-size:10px;line-height:1.35;color:var(--ink);white-space:nowrap}
  .contact-row{display:flex;gap:6px;align-items:flex-start;margin-bottom:8px}
  .contact-row svg{width:11px;height:11px;flex:none;margin-top:1px;fill:var(--ink)}

  /* letterhead */
  .letterhead{position:absolute;left:50px;top:104px;width:540px;height:764px;background:var(--paper);box-shadow:0 4px 14px rgba(0,0,0,.18);overflow:hidden}
  .letterhead .shapes{position:absolute;inset:0}
  .letterhead .brand{position:absolute;left:34px;top:70px}
  .letterhead .addresses{position:absolute;left:270px;top:552px;display:flex;gap:30px}

  /* cards */
  .card{position:absolute;width:500px;height:286px;background:var(--card);box-shadow:0 4px 14px rgba(0,0,0,.18);overflow:hidden}
  .card .shapes{position:absolute;inset:0}
  .card .brand{gap:7px}
  .card .brand-dot{width:24px;height:24px}
  .card .brand-name{font-size:11px}
  .card .brand-tag{font-size:5.5px}

  .business{left:650px;top:520px}
  .business .brand{position:absolute;left:22px;top:48px}
  .business .divider{position:absolute;left:258px;top:34px;width:2px;height:140px;background:var(--blue)}
  .business .addresses{position:absolute;left:272px;top:40px;display:flex;gap:10px}
  .business .contact{font-size:8px}
  .business .contact-row svg{width:9px;height:9px}
  .business .credential{position:absolute;left:24px;bottom:20px;font-family:"Noto Serif",serif;font-weight:700;font-size:10px;letter-spacing:1.6px;color:#fff}

  .appointment{left:650px;top:110px}
  .appointment .brand{position:absolute;left:24px;top:110px}
  .appointment .title{position:absolute;left:300px;top:24px;font-weight:700;font-size:20px;color:var(--ink)}
  .appointment .offices{position:absolute;left:300px;top:62px;display:flex;gap:18px;font-size:8.5px;white-space:nowrap}
  .office{display:flex;gap:5px;align-items:center}
  .office i{width:9px;height:9px;border:1px solid var(--ink);display:block}
  .fields{position:absolute;left:300px;top:84px;width:176px}
  .field{display:flex;align-items:flex-end;gap:6px;font-size:8.5px;height:26px}
  .field span{flex:1;border-bottom:1px solid var(--rule);height:1px;margin-bottom:3px}
  .appointment .note{position:absolute;left:24px;top:214px;font-size:8.5px;font-weight:500;letter-spacing:.5px;line-height:1.5;color:var(--ink);white-space:nowrap}
</style>
</head>
<body>

<svg class="icons" aria-hidden="true">
  <symbol id="icon-pin" viewBox="0 0 12 12"><path d="M6 0.5a4 4 0 0 0-4 4c0 3 4 7 4 7s4-4 4-7a4 4 0 0 0-4-4zm0 5.6a1.6 1.6 0 1 1 0-3.2 1.6 1.6 0 0 1 0 3.2z"/></symbol>
  <symbol id="icon-phone" viewBox="0 0 12 12"><path d="M1 3c0-1 1-2 2-2.2l1.4 2.4-1 1c.6 1.5 1.9 2.8 3.4 3.4l1-1L10.2 8C10 9 9 10 8 10 4.3 10 1 6.7 1 3z"/></symbol>
</svg>

<!-- Letterhead -->
<section class="letterhead">
  <svg class="shapes" viewBox="0 0 540 764" preserveAspectRatio="none" aria-hidden="true">
    <path d="M0 0H540V96C470 96 430 60 360 56L0 22Z" fill="var(--green)"/>
    <path d="M0 624H140C210 628 240 690 300 700L540 724V764H0Z" fill="var(--blue)"/>
  </svg>
  <div class="brand">
    <span class="brand-dot"></span>
    <div class="brand-text">
      <span class="brand-name">DANIEL R. HOLLISTER MD PC</span>
      <span class="brand-tag">ORTHOPAEDIC SURGERY &amp; SPORTS MEDICINE</span>
    </div>
  </div>
  <div class="addresses contact">
    <div>
      <div class="contact-row"><svg><use href="#icon-pin"/></svg><div>1874 Larkmoor Ave.<br>Suite KP7<br>Bronx, NY 10287</div></div>
      <div class="contact-row"><svg><use href="#icon-phone"/></svg><div>(718) 555 - 0142<br>(718) 555 - 0187</div></div>
    </div>
    <div>
      <div class="contact-row"><svg><use href="#icon-pin"/></svg><div>612 Ninth Ave.<br>Suite 42<br>New York, NY 10089</div></div>
      <div class="contact-row"><svg><use href="#icon-phone"/></svg><div>(212) 555 - 0163</div></div>
    </div>
  </div>
</section>

<!-- Appointment card -->
<section class="card appointment">
  <svg class="shapes" viewBox="0 0 500 286" preserveAspectRatio="none" aria-hidden="true">
    <path d="M0 0H90L0 10Z" fill="var(--green)"/>
    <path d="M500 120V286H320C370 286 380 250 400 200C420 150 450 130 500 120Z" fill="var(--sky)"/>
  </svg>
  <h1 class="title">Appointment</h1>
  <div class="offices">
    <label class="office"><i></i>Bronx office</label>
    <label class="office"><i></i>Manhattan office</label>
  </div>
  <div class="fields">
    <div class="field">For:<span></span></div>
    <div class="field">Date:<span></span></div>
    <div class="field">Time:<span></span></div>
  </div>
  <div class="brand">
    <span class="brand-dot"></span>
    <div class="brand-text">
      <span class="brand-name">DANIEL R. HOLLISTER MD PC</span>
      <span class="brand-tag">ORTHOPAEDIC SURGERY &amp; SPORTS MEDICINE</span>
    </div>
  </div>
  <p class="note">If you are unable to keep your appointment,<br>please call (718) 555-0129 24hrs in advance.</p>
</section>

<!-- Business card -->
<section class="card business">
  <svg class="shapes" viewBox="0 0 500 286" preserveAspectRatio="none" aria-hidden="true">
    <path d="M0 170C60 170 80 200 90 230C100 250 130 250 170 250H500V286H0Z" fill="var(--blue)"/>
    <path d="M500 160V250H470C470 200 450 170 400 160Z" fill="var(--green)"/>
  </svg>
  <div class="brand">
    <span class="brand-dot"></span>
    <div class="brand-text">
      <span class="brand-name">DANIEL R. HOLLISTER MD PC</span>
      <span class="brand-tag">ORTHOPAEDIC SURGERY &amp; SPORTS MEDICINE</span>
    </div>
  </div>
  <div class="divider"></div>
  <div class="addresses contact">
    <div>
      <div class="contact-row"><svg><use href="#icon-pin"/></svg><div>1874 Larkmoor Ave.<br>Suite KP7<br>Bronx, NY 10287</div></div>
      <div class="contact-row"><svg><use href="#icon-phone"/></svg><div>(718) 555 - 0142<br>(718) 555 - 0187</div></div>
    </div>
    <div>
      <div class="contact-row"><svg><use href="#icon-pin"/></svg><div>612 Ninth Ave.<br>Suite 42<br>New York, NY 10089</div></div>
      <div class="contact-row"><svg><use href="#icon-phone"/></svg><div>(212) 555 - 0163</div></div>
    </div>
  </div>
  <p class="credential">Board Certified American Orthopedic Surgery</p>
</section>

</body>
</html>
```